Business Card Design Project

Hello
I want a Simple Business card that uses the company logo that is easily reasonable but looks professional as I am an IT Services company and would look to share these cards with prospective clients.
The details are:
Kestrel Arc Solutions
14 Morrow Lane
Birmingham
B7 4QX
Telephone 0845 217 6640
I would like my name Oliver Hastings and my title Director on the card.
Target Market(s)
IT Professionals
Industry/Entity Type
Business

```html
<!DOCTYPE html>
<html lang="en">
<head>
<meta charset="utf-8">
<title>Kestrel Arc Solutions – Business Card</title>
<link rel="stylesheet" href="https://fonts.googleapis.com/css2?family=Open+Sans:wght@400;600&display=swap">
<style>
  :root {
    --page-bg: #e9e9e6;
    --card-white: #ffffff;
    --green-light: #66c435;
    --green-deep: #3f9f19;
    --accent-yellow: #f3c43f;
    --ink: #262626;
    --text-light: #ffffff;
  }
  * { box-sizing: border-box; margin: 0; padding: 0; }
  html, body {
    width: 1200px;
    height: 1200px;
    overflow: hidden;
    background: var(--page-bg);
    font-family: "Open Sans", Arial, sans-serif;
  }
  .business-card {
    position: absolute;
    left: 100px;
    top: 310px;
    width: 1000px;
    height: 580px;
    background: var(--card-white);
    box-shadow: 0 10px 30px rgba(0, 0, 0, 0.18);
    overflow: hidden;
  }
  .card-backdrop {
    position: absolute;
    inset: 0;
    width: 1000px;
    height: 580px;
  }
  .brand {
    position: absolute;
    left: 62px;
    top: 262px;
    display: flex;
    align-items: center;
    gap: 16px;
  }
  .brand-dot {
    width: 38px;
    height: 38px;
    border-radius: 50%;
    background: var(--green-light);
  }
  .brand-name {
    font-size: 35px;
    font-weight: 600;
    color: var(--ink);
    letter-spacing: -0.5px;
  }
  .holder {
    position: absolute;
    right: 62px;
    top: 104px;
    text-align: right;
    color: var(--text-light);
  }
  .holder-name {
    font-size: 44px;
    font-weight: 400;
    letter-spacing: 0.5px;
  }
  .holder-title {
    font-size: 30px;
    font-weight: 400;
    margin-top: 6px;
  }
  .contact {
    position: absolute;
    left: 610px;
    top: 318px;
    list-style: none;
    color: var(--text-light);
    font-size: 27px;
    line-height: 1.4;
  }
  .contact-item {
    display: flex;
    align-items: flex-start;
    gap: 18px;
    margin-bottom: 24px;
  }
  .contact-icon {
    flex: 0 0 28px;
    width: 28px;
    height: 38px;
    margin-top: 1px;
  }
</style>
</head>
<body>
  <article class="business-card">
    <svg class="card-backdrop" viewBox="0 0 1000 580" aria-hidden="true">
      <defs>
        <linearGradient id="white-panel" x1="0" y1="0" x2="1" y2="1">
          <stop offset="0" stop-color="#ffffff"/>
          <stop offset="1" stop-color="#efefef"/>
        </linearGradient>
        <linearGradient id="green-panel" x1="0" y1="0" x2="1" y2="1">
          <stop offset="0" stop-color="#6ac838"/>
          <stop offset="1" stop-color="#3c9c17"/>
        </linearGradient>
      </defs>
      <rect class="panel-white" width="1000" height="580" fill="url(#white-panel)"/>
      <polygon class="panel-green" points="612,0 1000,0 1000,580 512,580" fill="url(#green-panel)"/>
      <line class="accent-rule" x1="594" y1="0" x2="494" y2="580" stroke="var(--accent-yellow)" stroke-width="6"/>
    </svg>

    <div class="brand">
      <span class="brand-dot"></span>
      <span class="brand-name">Kestrel Arc Solutions</span>
    </div>

    <div class="holder">
      <p class="holder-name">Oliver Hastings</p>
      <p class="holder-title">Director</p>
    </div>

    <ul class="contact">
      <li class="contact-item">
        <svg class="contact-icon" viewBox="0 0 30 40" aria-hidden="true">
          <path d="M15 1C7.3 1 2 6.8 2 14c0 9.5 13 25 13 25s13-15.5 13-25C28 6.8 22.7 1 15 1z" fill="#ffffff"/>
          <circle cx="15" cy="14" r="5" fill="#52b227"/>
        </svg>
        <span class="contact-text">14 Morrow Lane<br>Birmingham, B7 4QX</span>
      </li>
      <li class="contact-item">
        <svg class="contact-icon" viewBox="0 0 30 40" aria-hidden="true">
          <path d="M7 6c2-1.5 3.5-1 4.5 1l2.5 5c.8 1.6.3 2.8-1 3.6l-1.6 1c.9 3.4 3 6.7 6 9l1.6-1c1.3-.8 2.6-.6 3.6.8l3 4.4c1 1.6.6 3-1 4l-2 1.3C16 38 3 22 3.5 11.5 3.7 9 5 7.3 7 6z" fill="#ffffff"/>
        </svg>
        <span class="contact-text">0845 217 6640</span>
      </li>
    </ul>
  </article>
</body>
</html>
```